Very High End Grooming Salon needs new business card design

I need a very nice card design I am a certified Master groomer we have a very high end clients. Our color is pink but does not have to be pink. I have a logo also a mission statement .
Fluff N Fern Pet Boutique and Spa
48810 Marlow Rd
Seabrook Cove fl 34019
555 904 3782
www.fluffernboutique.example
online booking available
this is our mission statement not sure it need to go on card but here it is.
Our Mission is to show respect to all animals pampering them with the same high end tailored service one would expect to receive at a day spa
as the only certified master groomer in the area we strive to put your pets best paw forward.

Industry/Entity Type

Business

```html
<!DOCTYPE html>
<html lang="en">
<head>
<meta charset="utf-8">
<title>Fluff N Fern Pet Boutique and Spa — Business Card</title>
<link href="https://fonts.googleapis.com/css2?family=Cormorant+Garamond:wght@500&family=Arimo:wght@400&display=swap" rel="stylesheet">
<style>
  :root {
    --backdrop: #8a8a8c;
    --card: #fbfbfa;
    --pink: #e0218a;
    --ink: #1c1c1c;
    --rule: #2a2a2a;
  }
  html, body {
    margin: 0;
    width: 1200px;
    height: 858px;
    overflow: hidden;
    background: var(--backdrop);
  }
  .canvas {
    width: 1200px;
    height: 858px;
    display: flex;
    align-items: center;
    justify-content: center;
    gap: 40px;
  }
  .card {
    width: 520px;
    height: 297px;
    background: var(--card);
    box-shadow: 0 6px 18px rgba(0,0,0,0.25);
    position: relative;
    box-sizing: border-box;
  }
  .card--back {
    display: flex;
    align-items: center;
  }
  .contact {
    flex: 1;
    padding-left: 46px;
    display: flex;
    flex-direction: column;
    gap: 7px;
    font-family: "Arimo", Arial, sans-serif;
    font-size: 15px;
    color: var(--ink);
  }
  .contact__row {
    display: flex;
    align-items: center;
    gap: 10px;
  }
  .contact__icon {
    width: 10px;
    height: 10px;
    flex: none;
    fill: var(--pink);
  }
  .contact__icon--blank { visibility: hidden; }
  .divider {
    width: 1px;
    height: 180px;
    background: var(--rule);
  }
  .brand-panel {
    flex: 1;
    display: flex;
    justify-content: center;
  }
  .brand {
    font-family: "Cormorant Garamond", Georgia, serif;
    font-weight: 500;
    color: var(--pink);
    text-align: center;
    line-height: 1.2;
  }
  .brand__name { font-size: 30px; display: block; }
  .brand__tag { font-size: 13px; letter-spacing: 1.5px; text-transform: uppercase; display: block; margin-top: 6px; }
  .card--front {
    display: flex;
    align-items: center;
    justify-content: center;
  }
  .card--front .brand__name { font-size: 40px; }
  .card--front .brand__tag { font-size: 15px; }
</style>
</head>
<body>
<main class="canvas">
  <section class="card card--back" aria-label="Card back with contact details">
    <div class="contact">
      <div class="contact__row">
        <svg class="contact__icon" viewBox="0 0 10 10"><path d="M2 0.5 L3.8 0.5 L4.4 2.8 L3.2 3.8 Q4.2 5.8 6.2 6.8 L7.2 5.6 L9.5 6.2 L9.5 8 Q9.5 9.5 8 9.5 Q1 9 0.5 2 Q0.5 0.5 2 0.5 Z"/></svg>
        <span>555 904 3782</span>
      </div>
      <div class="contact__row">
        <svg class="contact__icon" viewBox="0 0 10 10"><circle cx="5" cy="5" r="4.5"/></svg>
        <span>www.fluffernboutique.example</span>
      </div>
      <div class="contact__row">
        <svg class="contact__icon" viewBox="0 0 10 10"><path d="M5 0 A3.6 3.6 0 0 1 8.6 3.6 Q8.6 6 5 10 Q1.4 6 1.4 3.6 A3.6 3.6 0 0 1 5 0 Z"/></svg>
        <span>48810 Marlow Rd</span>
      </div>
      <div class="contact__row">
        <svg class="contact__icon contact__icon--blank" viewBox="0 0 10 10"></svg>
        <span>Seabrook Cove fl 34019</span>
      </div>
    </div>
    <div class="divider"></div>
    <div class="brand-panel">
      <div class="brand">
        <span class="brand__name">Fluff N Fern</span>
        <span class="brand__tag">Pet Boutique and Spa</span>
      </div>
    </div>
  </section>

  <section class="card card--front" aria-label="Card front">
    <div class="brand">
      <span class="brand__name">Fluff N Fern</span>
      <span class="brand__tag">Pet Boutique and Spa</span>
    </div>
  </section>
</main>
</body>
</html>
```